Mirela Causo Photography

I need a website design for my photography business, I want something clean, elegant, Classy.. I like the colors, White, Black, Green/Blue, Pink, Brown, Lavender,, I have a lot added my Logo .... Additional Info... I need a Photography Website Design, with probably 6 Tabs, Home, About Me, Portfolio, Gallery, Investment, Contact.
Home Page should have my logo, Name & Address, Social Media Icons, and Pictures.
As long as the templates are made I have a hosting coming that will code it.
Target Market(s)
Portraits Photography, Senior Portraits, Newborn, Families, Events, Engagements, Wedding,
Industry/Entity Type
Business
Number of Pages Required
5+ page
Look and feel

```html
<!DOCTYPE html>
<html lang="en">
<head>
<meta charset="utf-8">
<title>Mirela Causo Photography</title>
<link href="https://fonts.googleapis.com/css2?family=Oswald:wght@300;400;500&family=Roboto:wght@300;400&display=swap" rel="stylesheet">
<style>
:root{
  --black:#000;
  --footer:#111111;
  --footer-deep:#0b0b0b;
  --teal:#1ba089;
  --teal-dark:#178c78;
  --pink:#e56aa4;
  --white:#fff;
  --muted:#b8b8b8;
  --grey:#8a8a8a;
  --rule:#3a3a3a;
  --fb:#3b5998;--tw:#33a6dc;--yt:#c4302b;--gp:#d73d32;--rss:#f26522;
}
*{margin:0;padding:0;box-sizing:border-box}
html,body{width:1083px;height:1200px;overflow:hidden;background:var(--white)}
body{position:relative;font-family:'Roboto',sans-serif}
.abs{position:absolute}
/* header */
.site-header{position:absolute;left:0;top:0;width:1083px;height:91px;background:var(--black)}
.brand{position:absolute;left:99px;top:22px;color:var(--white);font-family:'Oswald',sans-serif;font-weight:500;font-size:19px;line-height:26px;letter-spacing:1px;text-transform:uppercase}
.main-nav a{position:absolute;top:40px;color:var(--white);font-family:'Oswald',sans-serif;font-weight:400;font-size:11.5px;text-decoration:none;text-transform:uppercase;transform:scaleX(.92);transform-origin:left}
.main-nav a.active{color:var(--pink)}
/* slider */
.hero{position:absolute;left:0;top:91px;width:1083px;height:513px;background:var(--teal)}
.frame{position:absolute;background:var(--white);box-shadow:0 14px 18px -10px rgba(0,0,0,.45)}
.frame .photo{position:absolute;inset:5px}
.slide-main{left:244px;top:31px;width:594px;height:434px}
.slide-main .photo{background:linear-gradient(180deg,#8e7f6c 0%,#6f6a5e 35%,#5d8491 60%,#4a5a6a 100%)}
.caption{position:absolute;left:5px;right:5px;bottom:5px;height:62px;background:rgba(40,40,55,.6);color:var(--white);font-family:'Oswald',sans-serif;font-weight:400;font-size:14.5px;text-align:center;line-height:62px;text-transform:uppercase;letter-spacing:-.2px}
.slide-l2{left:153px;top:79px;width:91px;height:339px}
.slide-l2 .photo{right:0;background:linear-gradient(180deg,#c9a98a,#b8412e 25%,#6a5a4d 55%,#3a3530)}
.slide-l1{left:99px;top:127px;width:55px;height:258px}
.slide-l1 .photo{right:0;background:linear-gradient(180deg,#a07c62,#d54a8a 50%,#5c3c3c)}
.slide-r2{left:838px;top:79px;width:92px;height:339px}
.slide-r2 .photo{left:0;background:linear-gradient(180deg,#cfd2d4,#9b8171 50%,#b89f8f)}
.slide-r1{left:930px;top:127px;width:52px;height:258px}
.slide-r1 .photo{left:0;background:linear-gradient(180deg,#c9483a,#d6d2cc 40%,#3b3b3b 70%,#d8d4cf)}
.arrow{position:absolute;top:250px;width:28px;height:28px}
/* about / portfolio */
.about{position:absolute;left:0;top:604px;width:1083px;height:176px;background:var(--black)}
.section-title{position:absolute;left:99px;font-family:'Oswald',sans-serif;font-weight:400;font-size:60px;letter-spacing:-2px;line-height:1}
.about .section-title{top:52px;color:var(--white)}
.divider{position:absolute;left:358px;width:1px}
.about .divider{top:28px;height:114px;background:var(--rule)}
.about-text{position:absolute;left:379px;top:30px;width:610px;font-size:10.5px;line-height:23.2px;color:var(--muted);font-weight:300}
.portfolio{position:absolute;left:0;top:780px;width:1083px;height:222px;background:var(--white)}
.portfolio .section-title{top:86px;color:var(--black)}
.portfolio .divider{top:58px;height:114px;background:#ddd}
.thumb{position:absolute;top:50px;width:189px;height:131px;background:var(--white);border:1px solid #e2e2e2}
.thumb::after{content:"";position:absolute;left:14px;right:14px;bottom:-8px;height:8px;border-radius:50%;background:rgba(0,0,0,.35);filter:blur(3px);z-index:-1}
.thumb .photo{position:absolute;inset:4px}
.t1{left:376px}.t1 .photo{background:linear-gradient(135deg,#9bb3c6,#3b6790 55%,#e7e6e2)}
.t2{left:585px}.t2 .photo{background:linear-gradient(135deg,#f2d546,#8bab2a 50%,#3d6f1e)}
.t3{left:794px}.t3 .photo{background:linear-gradient(160deg,#7fb1e0,#b7cfe8 40%,#8a5c4c 75%,#c0724e)}
/* footer */
.site-footer{position:absolute;left:0;top:1002px;width:1083px;height:132px;background:var(--footer)}
.footer-title{position:absolute;top:20px;color:var(--white);font-family:'Oswald',sans-serif;font-weight:400;font-size:17px;letter-spacing:-.3px;text-transform:uppercase}
.footer-small{position:absolute;color:#c9c9c9;font-size:10px;line-height:18px}
.footer-small.name{font-style:italic;color:var(--white);font-size:10.5px}
.email-input{position:absolute;left:477px;top:60px;width:176px;height:36px;background:var(--white);color:#9a9a9a;font-size:10px;line-height:36px;padding-left:12px}
.subscribe{position:absolute;left:653px;top:60px;width:101px;height:36px;background:var(--teal);color:var(--white);font-size:10px;line-height:36px;text-align:center;text-transform:uppercase}
.social{position:absolute;top:60px;width:34px;height:34px}
.bottom-bar{position:absolute;left:0;top:1134px;width:1083px;height:66px;background:var(--footer-deep)}
.bottom-links{position:absolute;left:100px;top:27px;color:#cfcfcf;font-size:10px;text-transform:uppercase}
.bottom-links span{margin:0 8px;color:#888}
.copyright{position:absolute;right:101px;top:27px;color:#6e6e6e;font-size:10.5px}
</style>
</head>
<body>
<header class="site-header">
  <div class="brand">Mirela Causo<br>Photography</div>
  <nav class="main-nav">
    <a class="active" style="left:526px">Home</a>
    <a style="left:594px">About Me</a>
    <a style="left:680px">Portfolio</a>
    <a style="left:769px">Gallery</a>
    <a style="left:848px">Investment</a>
    <a style="left:942px">Contact</a>
  </nav>
</header>

<section class="hero">
  <div class="frame slide-l1"><div class="photo" role="img" aria-label="Wedding party guests in a hall"></div></div>
  <div class="frame slide-l2"><div class="photo" role="img" aria-label="Floral centrepiece on a reception table"></div></div>
  <div class="frame slide-r1"><div class="photo" role="img" aria-label="Bride and groom at a ceremony"></div></div>
  <div class="frame slide-r2"><div class="photo" role="img" aria-label="Bride in a white dress"></div></div>
  <div class="frame slide-main">
    <div class="photo" role="img" aria-label="Couple sitting back to back beside a city fountain"></div>
    <div class="caption">Lorem ipsum dolor sit amet, consectetuer adipiscing elit</div>
  </div>
  <svg class="arrow" style="left:60px" viewBox="0 0 28 28"><circle cx="14" cy="14" r="14" fill="#111"/><path d="M16 9l-5 5 5 5" stroke="#fff" stroke-width="2" fill="none"/></svg>
  <svg class="arrow" style="left:992px" viewBox="0 0 28 28"><circle cx="14" cy="14" r="14" fill="#111"/><path d="M12 9l5 5-5 5" stroke="#fff" stroke-width="2" fill="none"/></svg>
</section>

<section class="about">
  <h2 class="section-title">ABOUT ME</h2>
  <div class="divider"></div>
  <p class="about-text">Lorem ipsum dolor sit amet, consectetuer adipiscing elit, sed diam nonummy nibh euismod tincidunt ut laoreet dolore magna aliquam erat volutpat. Ut wisi enim ad minim veniam, quis nostrud exerci tation ullamcorper suscipit lobortis nisl ut aliquip ex ea commodo consequat. Duis autem vel eum iriure dolor in hendrerit in vulputate velit esse molestie consequat, vel illum dolore eu feugiat nulla facilisis at vero eros et accumsan et iusto odio dignissim qui blandit praesent luptatum zzril delenit augue duis dolore te feugait nulla facilisi.</p>
</section>

<section class="portfolio">
  <h2 class="section-title">PORTFOLIO</h2>
  <div class="divider"></div>
  <div class="thumb t1"><div class="photo" role="img" aria-label="Woman sitting on a sailboat looking at the sea"></div></div>
  <div class="thumb t2"><div class="photo" role="img" aria-label="Family lying in sunny grass"></div></div>
  <div class="thumb t3"><div class="photo" role="img" aria-label="Group of friends giving thumbs up under a blue sky"></div></div>
</section>

<footer class="site-footer">
  <h3 class="footer-title" style="left:99px">Contact Us</h3>
  <svg class="abs" style="left:103px;top:58px" width="9" height="12" viewBox="0 0 9 12"><path d="M4.5 0A4.5 4.5 0 0 0 0 4.5C0 8 4.5 12 4.5 12S9 8 9 4.5A4.5 4.5 0 0 0 4.5 0z" fill="var(--pink)"/><circle cx="4.5" cy="4.5" r="1.7" fill="var(--footer)"/></svg>
  <div class="footer-small name" style="left:120px;top:55px">Mirela Causo Photography</div>
  <div class="footer-small" style="left:120px;top:73px">23, Lorem Ipsm,<br>Lorem Ipsm - 123 456</div>
  <svg class="abs" style="left:296px;top:62px" width="14" height="10" viewBox="0 0 14 10"><rect width="14" height="10" rx="1" fill="var(--pink)"/><path d="M0 1l7 5 7-5" stroke="var(--footer)" stroke-width="1.2" fill="none"/></svg>
  <div class="footer-small" style="left:318px;top:58px">hello@mirelacauso-studio.com</div>
  <svg class="abs" style="left:296px;top:84px" width="13" height="13" viewBox="0 0 13 13"><rect width="13" height="13" rx="2" fill="var(--pink)"/><path d="M4 3l1.5 2-1 1c.5 1 1.5 2 2.5 2.5l1-1 2 1.5-1 1.5C6.5 10.5 2.5 6.5 2.5 4z" fill="var(--footer)"/></svg>
  <div class="footer-small" style="left:318px;top:81px">(132) 555-0147</div>

  <h3 class="footer-title" style="left:476px">Newsletter Signup</h3>
  <div class="email-input">Email Address</div>
  <div class="subscribe">Subscribe</div>

  <h3 class="footer-title" style="left:779px">Connect Us</h3>
  <div class="social" style="left:779px;background:var(--fb)" role="img" aria-label="Social network link"></div>
  <div class="social" style="left:820px;background:var(--tw)" role="img" aria-label="Social network link"></div>
  <div class="social" style="left:862px;background:var(--yt)" role="img" aria-label="Video channel link"></div>
  <div class="social" style="left:905px;background:var(--gp)" role="img" aria-label="Social network link"></div>
  <div class="social" style="left:948px;background:var(--rss)" role="img" aria-label="News feed link"></div>
</footer>

<div class="bottom-bar">
  <div class="bottom-links">About Us<span>|</span>FAQ<span>|</span>Services</div>
  <div class="copyright">Copyright @ 2015 Mirela Causo Photography. All Right Reserved.</div>
</div>
</body>
</html>
```